Stretch on the Green with Mara

I want to advertise my Stretch on the Green classes for Summer. Classes are outside at the lovely local park. Dunmore field. 82 Halcombe St. Westlow.
Classes are for beginners to advance levels.
Classes start Monday, October 17th.
Monday 6pm Beginners
Tuesday 6pm Intermediate
Thursday 6pm Intermediate/Advance
Saturday 9am All fitness levels
My Pilates classes are specially designed to help improve strength and flexibility but as well will also improve posture, reduce stress and develop control and endurance in the entire body.
Booking essential. Limited numbers so I can make sure the correct technique is always being followed.
For more info or to book contact details:
Mara 027385916
mara@corestudiomara.net
www.corestudiomara.net
$15 Per Session

Target Market(s)

Males and Females ages 35plus.

Industry/Entity Type

Fitness

Font styles to use
Sans Serif

Requirements
Must have
• My logo. Contact details. A Park that looks lovely to exercise at.
Nice to have
• Summer looking. Trees - inspiration to be exercising outside

```html
<!DOCTYPE html>
<html lang="en">
<head>
<meta charset="utf-8">
<title>Stretch on the Green with Mara – Summer Classes</title>
<link rel="stylesheet" href="https://fonts.googleapis.com/css2?family=Arimo&family=Jost:wght@300;400;700&family=Nunito+Sans:wght@400&family=Roboto+Condensed:wght@300;400;700&family=Roboto+Slab:wght@400&display=swap">
<style>
  :root {
    --green: #00684f;
    --charcoal: #333334;
    --panel-grey: #616161;
    --logo-grey: #545454;
    --logo-pink: #e78bc8;
    --ink: #141414;
    --white: #ffffff;
    --text-light: #f2f2f2;
    --sky: #8fb7cf;
    --sea: #4f86b4;
    --tree: #6f8f3a;
    --grass: #86a845;
  }
  * { margin: 0; padding: 0; box-sizing: border-box; }
  html, body { width: 960px; height: 1200px; overflow: hidden; background: #ffffff; }
  .flyer {
    position: relative;
    width: 960px;
    height: 1200px;
    overflow: hidden;
    background: var(--charcoal);
    font-family: "Arimo", sans-serif;
  }

  /* Hero */
  .hero-photo {
    position: absolute; left: 0; top: 0; width: 960px; height: 455px;
    background: linear-gradient(180deg, var(--sea) 0%, #9fb89a 28%, var(--tree) 45%, var(--grass) 70%, #7d9c3c 100%);
  }
  .logo-box {
    position: absolute; left: 55px; top: 0; width: 318px; height: 150px;
    background: var(--logo-grey);
    display: flex; flex-direction: column; align-items: center; justify-content: center; gap: 14px;
  }
  .logo-mark { width: 30px; height: 30px; border-radius: 50%; background: #8c8c8c; }
  .logo-name {
    font-family: "Jost", sans-serif; font-weight: 400; font-size: 22px;
    letter-spacing: 1.5px; color: var(--logo-pink); text-transform: uppercase;
  }
  .headline {
    position: absolute; left: 54px; top: 178px;
    font-family: "Jost", sans-serif; font-weight: 700; font-size: 44px;
    color: var(--ink); line-height: 1; letter-spacing: 0.5px;
  }
  .subhead {
    position: absolute; left: 50px; top: 228px; width: 550px;
    font-family: "Jost", sans-serif; font-weight: 300; font-size: 33px;
    letter-spacing: 10px; color: var(--ink); line-height: 1;
    padding-bottom: 6px; border-bottom: 1px solid #3c3c3c;
  }
  .location {
    position: absolute; left: 55px; top: 282px;
    font-family: "Nunito Sans", sans-serif; font-size: 23px; line-height: 33px; color: var(--ink);
  }

  /* Service strip */
  .services {
    position: absolute; left: 3px; top: 453px; width: 954px;
    display: flex; gap: 4px;
  }
  .service { flex: 1; }
  .service-photo { height: 146px; }
  .service-label {
    height: 48px; background: var(--green); color: var(--white);
    font-family: "Roboto Condensed", sans-serif; font-weight: 700; font-size: 15px;
    text-transform: uppercase; text-align: center; line-height: 19px;
    display: flex; align-items: center; justify-content: center;
  }
  .tone-1 { background: linear-gradient(160deg, #d9d2c8, #7a6a5c 60%, #4a3a30); }
  .tone-2 { background: linear-gradient(160deg, #f1efeb, #d8d2c9 55%, #8b3a44); }
  .tone-3 { background: linear-gradient(160deg, #e9e7e3, #8c8a86 50%, #2b2b2b); }
  .tone-4 { background: linear-gradient(160deg, #c9ccd0, #e9e7e6 50%, #5c7ea5); }
  .tone-5 { background: linear-gradient(160deg, #ffffff, #f3efe9 55%, #d9c8b8); }

  /* Info */
  .about {
    position: absolute; left: 42px; top: 683px; width: 470px;
    font-size: 20.5px; line-height: 26px; color: var(--text-light);
  }
  .contact-heading {
    position: absolute; left: 42px; top: 836px;
    font-family: "Roboto Slab", serif; font-size: 22px; line-height: 30px;
    color: var(--white); text-transform: uppercase;
  }
  .contact-list {
    position: absolute; left: 42px; top: 913px;
    font-family: "Roboto Slab", serif; font-size: 19px; line-height: 27px;
    color: var(--white); list-style: none;
  }
  .price {
    position: absolute; left: 38px; top: 1030px; width: 240px; height: 38px;
    background: var(--green); border-radius: 0 20px 20px 0;
    font-family: "Jost", sans-serif; font-weight: 700; font-size: 21px; color: var(--white);
    display: flex; align-items: center; justify-content: center;
  }

  .schedule {
    position: absolute; left: 528px; top: 679px; width: 394px; height: 386px;
    background: var(--panel-grey); border-radius: 4px; overflow: hidden;
  }
  .schedule-head {
    background: var(--green); height: 66px; padding: 8px 0 0 21px;
    font-family: "Roboto Condensed", sans-serif; font-weight: 700; font-size: 23px;
    line-height: 25px; color: var(--white); text-transform: uppercase;
  }
  .schedule-start {
    margin: 22px 0 10px 19px;
    font-family: "Roboto Condensed", sans-serif; font-weight: 300; font-size: 21px; color: var(--white);
  }
  .schedule-list { list-style: none; margin-left: 25px; }
  .schedule-item {
    position: relative; padding-left: 26px; margin-bottom: 8px;
    font-family: "Roboto Condensed", sans-serif; font-weight: 300; font-size: 21px;
    line-height: 26px; color: var(--white);
  }
  .schedule-item::before {
    content: ""; position: absolute; left: 0; top: 9px;
    width: 9px; height: 9px; border-radius: 50%; background: var(--white);
  }

  /* Footer */
  .footer-wave { position: absolute; left: 0; top: 1080px; width: 960px; height: 120px; }
  .footer-url {
    position: absolute; right: 56px; top: 1141px;
    font-family: "Roboto Slab", serif; font-size: 19px; color: var(--white);
  }
</style>
</head>
<body>
<main class="flyer">
  <div class="hero-photo" role="img" aria-label="Woman stretching on the grass of a sunny seaside park with trees and a bench"></div>

  <div class="logo-box">
    <span class="logo-mark"></span>
    <span class="logo-name">Stretch with Mara</span>
  </div>

  <h1 class="headline">STRETCH ON THE GREEN</h1>
  <p class="subhead">CLASSES FOR SUMMER.</p>
  <p class="location">Classes are outside at the lovely local park.<br>Dunmore field. 82 Halcombe St. Westlow.</p>

  <section class="services">
    <div class="service">
      <div class="service-photo tone-1" role="img" aria-label="Woman doing a bridge exercise on a mat at home"></div>
      <div class="service-label">Group Pilates<br>Classes</div>
    </div>
    <div class="service">
      <div class="service-photo tone-2" role="img" aria-label="Man and woman stretching arms overhead in a living room"></div>
      <div class="service-label">Mobile Private<br>Pilates Sessions</div>
    </div>
    <div class="service">
      <div class="service-photo tone-3" role="img" aria-label="Group doing a lunge stretch together in a studio"></div>
      <div class="service-label">Group Mobile<br>Pilates Sessions</div>
    </div>
    <div class="service">
      <div class="service-photo tone-4" role="img" aria-label="Mothers exercising on mats with babies beside them"></div>
      <div class="service-label">Postnatal Mobile<br>Pilates Classes</div>
    </div>
    <div class="service">
      <div class="service-photo tone-5" role="img" aria-label="Mother lifting her baby while exercising on the floor"></div>
      <div class="service-label">Mums and Bubs<br>Class</div>
    </div>
  </section>

  <p class="about">My Pilates classes are specially designed to help improve strength and flexibility but as well will also improve posture, reduce stress and develop control &amp; endurance in the entire body.</p>

  <h2 class="contact-heading">For more info or to book<br>contact details:</h2>
  <ul class="contact-list">
    <li>Mara 027385916</li>
    <li>mara@corestudiomara.net</li>
    <li>www.corestudiomara.net</li>
  </ul>

  <div class="price">$15 PER SESSION</div>

  <section class="schedule">
    <h2 class="schedule-head">Classes are for<br>beginners to advance levels.</h2>
    <p class="schedule-start">Classes start Monday, October 17th.</p>
    <ul class="schedule-list">
      <li class="schedule-item">Monday 6pm<br>Beginners</li>
      <li class="schedule-item">Tuesday 6pm<br>Intermediate</li>
      <li class="schedule-item">Thursday 6pm<br>Intermediate/Advance</li>
      <li class="schedule-item">Saturday 9am<br>All fitness levels</li>
    </ul>
  </section>

  <svg class="footer-wave" viewBox="0 0 960 120" preserveAspectRatio="none" aria-hidden="true">
    <path d="M0,30 C70,80 240,92 480,62 S850,4 960,6 L960,120 L0,120 Z" fill="#d9d9d9"/>
    <path d="M0,44 C80,94 250,96 480,68 S850,12 960,14 L960,120 L0,120 Z" fill="var(--green)"/>
  </svg>
  <p class="footer-url">www.corestudiomara.net</p>
</main>
</body>
</html>
```